UI Design for a pre-ordering & Universal loyalty mobile app

We have built a central universal, preordering and gamification mobile app for alot of F&B merchant. The app is called TRIVU (Trivoo as in eating something fast). Main goal for this app is too
1. Give users a universal loyalty system where they can accumulate loyalty points and use it on any brands
2. Gives user the ability to preorder for their food or drinks on the app and pick it up instore
3. There will be an E-wallet that is general or there can be a brand e-wallet (where they top-up with the brand only and get extra bonus)
4. There will be promotion such as games, top-up bonuses and rewards.
5. Community app where they can send money or promotion to their friends and will be able to play games together
This app is developed on the Flutter framework and also uses fontawesome font/icon package. Please consider this when doing the UI design for the app.
We are planning to create a mascot for our app as well and when it comes to color and icon, it's not set in stone and we are open for ideas.
I will attached our app icon and a few of our screens for your reference and each page details as follows:
Navigation bar.
There is a navigation bar on the top that should be visible on all screen. On the left will be a button to enter the menu which gives user more option and on the right will be a place for them to scan their QR code for loyalty points or payment and also a button to access their e-wallet.
1. Home screen
This screen is basically the main screen after user login. In this screen there will be
- Main banner (main promotions that's controlled by us)
- Specials banner (smaller) that will be controlled by the store/brands
- Favourite Store or Favourite food/drinks that user pre-configure
2. Shop screen (or can be called something else)
This screen is where they can browse all our participating stores. This screen will include
- Categories (filter)
- Brands which user can click and only view the brand page and stores
- All stores sorted by distances
3. Brand screen
The brand screen gives our brand with multiple store a presense on the app that is branded for them. They can have their own color scheme, logo and will only display their own store
4. Store screen
This will display all the store details, opening time, location, contact information etc.
- This screen will contain a banner/store image
- Store details
- Categories
- Food/drinks within the category
5. Order history screen
This will display their current order or their past order. Not sure if it should be on the main navigation or the sub navigation.
When making the UI design, please work on a color theme that will suit and also consider a mascot design in the future.
Feel free to ask me any questions before proceeding.
Thanks

```html
<!DOCTYPE html>
<html lang="en">
<head>
<meta charset="utf-8">
<title>TRIVU app screens</title>
<link rel="stylesheet" href="https://fonts.googleapis.com/css2?family=Roboto:wght@400;500;700&display=swap">
<style>
:root{
  --bg-top:#c90a2c;
  --bg-bottom:#9c0440;
  --brand-red:#c8102e;
  --brand-green:#a3b40a;
  --ink:#2b2b2b;
  --muted:#6f6f6f;
  --line:#e6e6e6;
  --white:#ffffff;
  --chip-cream:#f4f1df;
}
*{box-sizing:border-box;margin:0;padding:0}
html,body{width:1200px;height:761px;overflow:hidden}
body{
  font-family:'Roboto',sans-serif;
  background:linear-gradient(180deg,var(--bg-top),var(--bg-bottom));
  position:relative;color:var(--ink);
}
.icons{position:absolute;width:0;height:0}
.screen{
  position:absolute;top:95px;width:375px;height:810px;
  transform:scale(.704);transform-origin:0 0;
  background:var(--white);border-radius:34px;overflow:hidden;
}
.screen--home{left:105px}
.screen--shop{left:469px}
.screen--orders{left:833px}
.abs{position:absolute}
.topbar{position:absolute;left:0;top:0;width:375px;height:100px;background:var(--brand-red)}
.topbar__time{position:absolute;left:22px;top:11px;color:#fff;font-size:14px;font-weight:500}
.topbar__status{position:absolute;right:22px;top:12px;width:60px;height:14px}
.round-btn{position:absolute;top:49px;width:32px;height:32px;border-radius:50%;background:#fff;display:flex;align-items:center;justify-content:center}
.round-btn--menu{left:36px}
.round-btn--scan{left:283px;background:var(--brand-green)}
.round-btn--wallet{left:320px}
.round-btn svg{width:16px;height:16px}
.brandmark{
  position:absolute;left:124px;top:38px;width:126px;height:126px;border-radius:50%;
  background:#fff;border:6px solid var(--brand-red);
  display:flex;align-items:flex-end;justify-content:center;padding-bottom:24px;
}
.brandmark__name{font-size:18px;font-weight:500;letter-spacing:4px;color:var(--brand-red)}
.section-title{position:absolute;left:21px;font-size:20px;font-weight:500;text-transform:uppercase;color:var(--ink)}
.photo{position:absolute;overflow:hidden}
.hero{left:0;top:167px;width:375px;height:200px;background:linear-gradient(120deg,#3a2a22,#7a4a2a 45%,#b9743a 70%,#2d2a2c)}
.hero__text{position:absolute;left:21px;top:218px;color:#fff;font-size:23px;font-weight:500;line-height:33px;text-transform:uppercase;width:260px}
.deal{top:425px;height:96px;border-radius:6px}
.deal--one{left:24px;width:196px;background:linear-gradient(110deg,#35475c,#c9a07a 50%,#f1d3a5)}
.deal--two{left:244px;width:140px;background:linear-gradient(110deg,#5a5e63,#d8d4cc 50%,#a87a55)}
.fav{left:24px;top:581px;width:326px;height:146px;border-radius:10px;background:linear-gradient(120deg,#6b5443,#b48a62 45%,#e4d2b8 70%,#7d6150)}
.pill{position:absolute;background:#fff;border-radius:20px;display:flex;align-items:center;justify-content:center;font-size:11px;color:var(--ink)}
.fav__bonus{left:37px;top:686px;width:150px;height:30px}
.circle-ico{position:absolute;width:32px;height:32px;border-radius:50%;display:flex;align-items:center;justify-content:center}
.circle-ico svg{width:14px;height:14px}
.fav__star{left:267px;top:685px;background:var(--brand-green)}
.fav__pin{left:305px;top:685px;background:#fff}
.navbar{position:absolute;left:0;top:749px;width:375px;height:61px;background:var(--brand-green)}
.navbar__item{position:absolute;top:8px;width:44px;height:44px;border-radius:50%;display:flex;align-items:center;justify-content:center}
.navbar__item svg{width:22px;height:22px;fill:#fff}
.navbar__item--active{background:#fff}
.navbar__item--active svg{fill:var(--brand-green)}
.navbar__item:nth-child(1){left:22px}
.navbar__item:nth-child(2){left:116px}
.navbar__item:nth-child(3){left:211px}
.navbar__item:nth-child(4){left:306px}
.search{position:absolute;left:23px;top:187px;width:327px;height:36px;border:2px solid #eee;border-radius:20px;box-shadow:0 2px 6px rgba(0,0,0,.08);display:flex;align-items:center;padding-left:14px;font-size:12px;color:#444;gap:8px}
.search svg{width:12px;height:12px}
.chip{position:absolute;top:296px;height:34px;border-radius:20px;border:2px solid #eee;box-shadow:0 2px 6px rgba(0,0,0,.08);display:flex;align-items:center;justify-content:center;font-size:12px;font-weight:500;color:#444;background:#fff}
.chip--active{background:var(--brand-green);border-color:var(--brand-green);color:#fff}
.brand-tile{position:absolute;top:391px;width:68px;height:68px;box-shadow:0 2px 6px rgba(0,0,0,.15);border:3px solid #fff}
.store{position:absolute;left:23px;width:327px;height:108px;background:#fff;box-shadow:0 2px 8px rgba(0,0,0,.12)}
.store__photo{position:absolute;left:2px;top:4px;width:100px;height:100px;border-radius:50%;background:linear-gradient(135deg,#2e3236,#7b5a3e 50%,#c39b6c);border:4px solid #fff}
.store__name{position:absolute;left:117px;top:12px;font-size:13px;font-weight:500;text-transform:uppercase}
.store__meta{position:absolute;left:117px;font-size:11px;color:#444;display:flex;align-items:center;gap:5px;white-space:nowrap}
.store__meta svg{width:10px;height:10px;fill:var(--brand-red)}
.store__eta{position:absolute;left:55px;top:90px;height:26px;padding:0 14px;background:var(--chip-cream);border-radius:14px;font-size:11px;display:flex;align-items:center;gap:6px}
.store__eta svg{width:10px;height:10px;fill:var(--brand-green)}
.tab{position:absolute;top:224px;height:36px;border-radius:20px;font-size:12px;font-weight:500;display:flex;align-items:center;justify-content:center;border:2px solid #eee;box-shadow:0 2px 6px rgba(0,0,0,.08);background:#fff;color:#333}
.tab--active{background:var(--brand-green);border-color:var(--brand-green);color:#fff}
.order{position:absolute;left:22px;width:328px;height:110px;background:#fff;border:2px solid #eee;box-shadow:0 2px 6px rgba(0,0,0,.08)}
.order__photo{position:absolute;left:0;top:0;width:108px;height:106px}
.order__name{position:absolute;left:124px;top:8px;font-size:13px;font-weight:500;text-transform:uppercase}
.order__addr{position:absolute;left:124px;top:29px;font-size:11px;color:#555;display:flex;align-items:center;gap:5px}
.order__addr svg{width:10px;height:10px;fill:var(--brand-green)}
.order__status{position:absolute;left:124px;top:50px;width:84px;height:29px;background:var(--chip-cream);font-size:9px;color:#444;display:flex;align-items:center;justify-content:center}
.order__reorder{position:absolute;left:215px;top:50px;width:86px;height:29px;background:var(--brand-red);border-radius:4px;color:#fff;font-size:9px;font-weight:700;display:flex;align-items:center;justify-content:center;gap:4px}
.order__reorder svg{width:9px;height:9px;fill:#fff}
.order__rating{position:absolute;left:124px;top:87px;font-size:7px;color:#555;display:flex;align-items:center;gap:4px}
.stars{color:#f2a900;font-size:9px;letter-spacing:1px}
</style>
</head>
<body>

<svg class="icons" aria-hidden="true">
  <defs>
    <symbol id="i-menu" viewBox="0 0 16 16"><rect x="2" y="3" width="12" height="2" rx="1"/><rect x="2" y="7" width="12" height="2" rx="1"/><rect x="2" y="11" width="12" height="2" rx="1"/></symbol>
    <symbol id="i-scan" viewBox="0 0 16 16"><rect x="2" y="2" width="5" height="5" fill="none" stroke="#fff" stroke-width="1.5"/><rect x="9" y="2" width="5" height="5" fill="none" stroke="#fff" stroke-width="1.5"/><rect x="2" y="9" width="5" height="5" fill="none" stroke="#fff" stroke-width="1.5"/><rect x="9" y="9" width="2" height="2" fill="#fff"/><rect x="12" y="12" width="2" height="2" fill="#fff"/></symbol>
    <symbol id="i-card" viewBox="0 0 16 16"><rect x="1.5" y="3.5" width="13" height="9" rx="1.5" fill="none" stroke="#333" stroke-width="1.3"/><rect x="1.5" y="6" width="13" height="1.6" fill="#333"/></symbol>
    <symbol id="i-home" viewBox="0 0 24 24"><path d="M12 3 2 12h3v8h5v-5h4v5h5v-8h3z"/></symbol>
    <symbol id="i-basket" viewBox="0 0 24 24"><path d="M9 3 6 9H2v3h1l2 9h14l2-9h1V9h-4l-3-6-1.5.8L16 9H8l2.5-5.2z M8 13h2v6H8z M11 13h2v6h-2z M14 13h2v6h-2z"/></symbol>
    <symbol id="i-list" viewBox="0 0 24 24"><rect x="3" y="4" width="4" height="4"/><rect x="9" y="4" width="12" height="4"/><rect x="3" y="10" width="4" height="4"/><rect x="9" y="10" width="12" height="4"/><rect x="3" y="16" width="4" height="4"/><rect x="9" y="16" width="12" height="4"/></symbol>
    <symbol id="i-game" viewBox="0 0 24 24"><path d="M7 7h10a5 5 0 0 1 0 10c-1.8 0-2.6-1.5-3.5-2h-3C9.6 15.5 8.8 17 7 17A5 5 0 0 1 7 7zm-1 3v1.5H4.5v1.5H6v1.5h1.5V13H9v-1.5H7.5V10zm10 .5a1 1 0 1 0 0 2 1 1 0 0 0 0-2zm2.2 1.5a1 1 0 1 0 0 2 1 1 0 0 0 0-2z"/></symbol>
    <symbol id="i-star" viewBox="0 0 16 16"><path d="M8 1.5l2 4.2 4.6.6-3.3 3.2.8 4.5L8 11.8 3.9 14l.8-4.5L1.4 6.3 6 5.7z"/></symbol>
    <symbol id="i-pin" viewBox="0 0 16 16"><path d="M8 1a5 5 0 0 0-5 5c0 3.5 5 9 5 9s5-5.5 5-9a5 5 0 0 0-5-5zm0 7a2 2 0 1 1 0-4 2 2 0 0 1 0 4z"/></symbol>
    <symbol id="i-phone" viewBox="0 0 16 16"><path d="M3.6 1.5 6 4 4.8 5.9a9 9 0 0 0 5.3 5.3L12 10l2.5 2.4-1.6 2.1C7.2 14.3 1.7 8.8 1.5 3.1z"/></symbol>
    <symbol id="i-clock" viewBox="0 0 16 16"><path d="M8 1a7 7 0 1 0 0 14A7 7 0 0 0 8 1zm0 2a5 5 0 1 1 0 10A5 5 0 0 1 8 3zm-.8 1.5v4.3l3.2 2 .8-1.2-2.5-1.5V4.5z"/></symbol>
    <symbol id="i-search" viewBox="0 0 16 16"><circle cx="7" cy="7" r="5" fill="none" stroke="#333" stroke-width="2"/><path d="M10.5 10.5 15 15" stroke="#333" stroke-width="2"/></symbol>
    <symbol id="i-redo" viewBox="0 0 16 16"><path d="M8 2a6 6 0 1 0 5.7 7.9h-2.2A4 4 0 1 1 10.8 5L9 7h5V2l-1.8 1.8A6 6 0 0 0 8 2z"/></symbol>
    <symbol id="i-status" viewBox="0 0 60 14"><rect x="0" y="9" width="3" height="4" fill="#fff"/><rect x="4" y="6" width="3" height="7" fill="#fff"/><rect x="8" y="3" width="3" height="10" fill="#fff"/><path d="M18 5a9 9 0 0 1 12 0l-1.5 1.5a7 7 0 0 0-9 0zM20.5 8a5 5 0 0 1 7 0L24 12z" fill="#fff"/><rect x="36" y="2" width="20" height="10" rx="2.5" fill="none" stroke="#fff"/><rect x="38" y="4" width="16" height="6" rx="1" fill="#fff"/></symbol>
  </defs>
</svg>

<!-- Home -->
<section class="screen screen--home">
  <header class="topbar">
    <span class="topbar__time">12:00</span>
    <svg class="topbar__status"><use href="#i-status"/></svg>
    <span class="round-btn round-btn--menu"><svg fill="#333"><use href="#i-menu"/></svg></span>
    <span class="round-btn round-btn--scan"><svg><use href="#i-scan"/></svg></span>
    <span class="round-btn round-btn--wallet"><svg><use href="#i-card"/></svg></span>
  </header>
  <div class="brandmark"><span class="brandmark__name">TRIVU</span></div>

  <div class="photo hero" role="img" aria-label="Warm restaurant interior with pendant lights"></div>
  <p class="hero__text">Trivoo as in eating something fast</p>

  <h2 class="section-title" style="top:385px">Deals</h2>
  <div class="photo deal deal--one" role="img" aria-label="Café counter with a barista serving a customer"></div>
  <div class="photo deal deal--two" role="img" aria-label="Barista standing at a coffee bar"></div>

  <h2 class="section-title" style="top:545px">Favourites</h2>
  <div class="photo fav" role="img" aria-label="Bright café interior with bar stools and shelves"></div>
  <span class="pill fav__bonus">100% Deposite Bonus</span>
  <span class="circle-ico fav__star"><svg fill="#fff"><use href="#i-star"/></svg></span>
  <span class="circle-ico fav__pin"><svg fill="#333"><use href="#i-pin"/></svg></span>

  <nav class="navbar">
    <span class="navbar__item navbar__item--active"><svg><use href="#i-home"/></svg></span>
    <span class="navbar__item"><svg><use href="#i-basket"/></svg></span>
    <span class="navbar__item"><svg><use href="#i-list"/></svg></span>
    <span class="navbar__item"><svg><use href="#i-game"/></svg></span>
  </nav>
</section>

<!-- Shop -->
<section class="screen screen--shop">
  <header class="topbar">
    <span class="topbar__time">12:00</span>
    <svg class="topbar__status"><use href="#i-status"/></svg>
    <span class="round-btn round-btn--menu"><svg fill="#333"><use href="#i-menu"/></svg></span>
    <span class="round-btn round-btn--scan"><svg><use href="#i-scan"/></svg></span>
    <span class="round-btn round-btn--wallet"><svg><use href="#i-card"/></svg></span>
  </header>
  <div class="brandmark"><span class="brandmark__name">TRIVU</span></div>

  <div class="search"><svg><use href="#i-search"/></svg>Search...</div>

  <h2 class="section-title" style="top:255px">Categories</h2>
  <span class="chip" style="left:23px;width:73px">TEA</span>
  <span class="chip chip--active" style="left:103px;width:114px">BUBBLE TEA</span>
  <span class="chip" style="left:230px;width:81px">COFFEE</span>
  <span class="chip" style="left:323px;width:90px;justify-content:flex-start;padding-left:14px">SNACKS</span>

  <h2 class="section-title" style="top:355px">Brands</h2>
  <span class="brand-tile" style="left:23px;background:#1f6fb0"></span>
  <span class="brand-tile" style="left:110px;background:#22357a"></span>
  <span class="brand-tile" style="left:196px;background:#8cc63f"></span>
  <span class="brand-tile" style="left:282px;background:#1f8a5b"></span>

  <h2 class="section-title" style="top:483px">Stores near you</h2>

  <article class="store" style="top:522px">
    <div class="store__photo" role="img" aria-label="Store interior"></div>
    <h3 class="store__name">Demo 2 Perth</h3>
    <p class="store__meta" style="top:32px">Tea &nbsp;|&nbsp; Bubble Tea &nbsp;|&nbsp; Burgers</p>
    <p class="store__meta" style="top:51px"><svg><use href="#i-pin"/></svg>123 A Street Somewhere Here</p>
    <p class="store__meta" style="top:70px"><svg><use href="#i-phone"/></svg>+1 (555) 010 0000 &nbsp;|&nbsp; <svg><use href="#i-clock"/></svg>9am -6pm</p>
    <span class="store__eta"><svg><use href="#i-clock"/></svg>5 Mins &nbsp;|&nbsp; <svg><use href="#i-pin"/></svg>1.24km</span>
  </article>

  <article class="store" style="top:658px">
    <div class="store__photo" role="img" aria-label="Store interior"></div>
    <h3 class="store__name">Leafline Broadway</h3>
    <p class="store__meta" style="top:32px">Tea &nbsp;|&nbsp; Bubble Tea &nbsp;|&nbsp; Burgers</p>
    <p class="store__meta" style="top:51px"><svg><use href="#i-pin"/></svg>123 A Street Somewhere Here</p>
    <p class="store__meta" style="top:70px"><svg><use href="#i-phone"/></svg>+1 (555) 010 0000 &nbsp;|&nbsp; <svg><use href="#i-clock"/></svg>9am -6pm</p>
  </article>

  <nav class="navbar">
    <span class="navbar__item"><svg><use href="#i-home"/></svg></span>
    <span class="navbar__item navbar__item--active"><svg><use href="#i-basket"/></svg></span>
    <span class="navbar__item"><svg><use href="#i-list"/></svg></span>
    <span class="navbar__item"><svg><use href="#i-game"/></svg></span>
  </nav>
</section>

<!-- Order history -->
<section class="screen screen--orders">
  <header class="topbar">
    <span class="topbar__time">12:00</span>
    <svg class="topbar__status"><use href="#i-status"/></svg>
    <span class="round-btn round-btn--menu"><svg fill="#333"><use href="#i-menu"/></svg></span>
    <span class="round-btn round-btn--scan"><svg><use href="#i-scan"/></svg></span>
    <span class="round-btn round-btn--wallet"><svg><use href="#i-card"/></svg></span>
  </header>
  <div class="brandmark"><span class="brandmark__name">TRIVU</span></div>

  <h2 class="section-title" style="top:180px">Order history</h2>
  <span class="tab" style="left:23px;width:117px">QUEUE</span>
  <span class="tab tab--active" style="left:154px;width:114px">COMPLETED</span>

  <article class="order" style="top:287px">
    <div class="photo order__photo" role="img" aria-label="Cup of coffee on a table" style="background:linear-gradient(120deg,#3b3430,#a58d74 55%,#d9cbb8)"></div>
    <h3 class="order__name">Leafline Broadway</h3>
    <p class="order__addr"><svg><use href="#i-pin"/></svg>123 A Street Somewhere Here</p>
    <span class="order__status">DELIVERED</span>
    <span class="order__reorder"><svg><use href="#i-redo"/></svg>REORDER</span>
    <p class="order__rating"><span class="stars">★★★★★</span>(112 Reviews)</p>
  </article>

  <article class="order" style="top:414px">
    <div class="photo order__photo" role="img" aria-label="Croissants beside a coffee cup" style="background:linear-gradient(120deg,#f0ece6,#c98a3c 45%,#2a211c)"></div>
    <h3 class="order__name">Leafline Broadway</h3>
    <p class="order__addr"><svg><use href="#i-pin"/></svg>123 A Street Somewhere Here</p>
    <span class="order__status">DELIVERED</span>
    <span class="order__reorder"><svg><use href="#i-redo"/></svg>REORDER</span>
    <p class="order__rating"><span class="stars">★★★★★</span>(112 Reviews)</p>
  </article>

  <article class="order" style="top:540px">
    <div class="photo order__photo" role="img" aria-label="Coffee bag with scattered beans" style="background:linear-gradient(120deg,#1e1814,#6b4a33 45%,#c8ad8a 65%,#2a1f18)"></div>
    <h3 class="order__name">Leafline Broadway</h3>
    <p class="order__addr"><svg><use href="#i-pin"/></svg>123 A Street Somewhere Here</p>
    <span class="order__status">DELIVERED</span>
    <span class="order__reorder"><svg><use href="#i-redo"/></svg>REORDER</span>
    <p class="order__rating"><span class="stars">★★★★★</span>(112 Reviews)</p>
  </article>

  <article class="order" style="top:667px">
    <div class="photo order__photo" role="img" aria-label="Latte art being poured into a cup" style="background:linear-gradient(120deg,#2b2623,#8a6a4e 50%,#e8ddd0)"></div>
    <h3 class="order__name">Leafline Broadway</h3>
    <p class="order__addr"><svg><use href="#i-pin"/></svg>123 A Street Somewhere Here</p>
    <span class="order__status">DELIVERED</span>
    <span class="order__reorder"><svg><use href="#i-redo"/></svg>REORDER</span>
  </article>

  <nav class="navbar">
    <span class="navbar__item"><svg><use href="#i-home"/></svg></span>
    <span class="navbar__item"><svg><use href="#i-basket"/></svg></span>
    <span class="navbar__item navbar__item--active"><svg><use href="#i-list"/></svg></span>
    <span class="navbar__item"><svg><use href="#i-game"/></svg></span>
  </nav>
</section>

</body>
</html>
```